Brivane Communications - veteran and exclusive boutique copywriting agency

PROJECT NEEDS:
1. Website design - full homepage design and inner page top banner design
2. Logo design
* Please see attached Briefs (Word Docs) for descriptions of what is needed for 1 and 2 above.
ABOUT THE CLIENT:
Brivane Communications is a veteran and exclusive boutique copywriting agency run by Martin Olafsky. Martin is an award-winning published novelist and an accomplished executive ghostwriter with articles regularly published prominent technology publications like Pulsar, ByteHarbor, CapitalDrift, and more. For nearly three decades, Martin has focused solely on the technology sector - serving clients in Israel, Europe and the US.

Target Market(s)

hi-tech companies run by serious, confident professionals.

Industry/Entity Type

Business

Number of Pages Required

2 page

Font styles to use
Sans Serif
Other font styles liked:
• font should be modern

Colors
0054AA
0677BA
7BADD7
CADEEF
E8F1F8
F0912C
F2A743
F7CA91
FBE8D2
FDF5EE

Requirements
Must have
• psd files for logo, homepage design, and inner page top banner design
Nice to have
• Please see attached Website and Logo Design Briefs (Word Docs)
Should not have

```html
<!DOCTYPE html>
<html lang="en">
<head>
<meta charset="utf-8">
<title>Brivane Communications</title>
<link rel="stylesheet" href="https://fonts.googleapis.com/css2?family=Jost:ital,wght@0,400;0,500;0,600;0,700;1,400&display=swap">
<style>
:root{
  --dark:#3a3f4b;
  --darker:#1f2431;
  --orange:#ef6a0c;
  --ink:#2f3440;
  --text:#3a3a3a;
  --light:#f7f7f8;
  --white:#ffffff;
}
*{margin:0;padding:0;box-sizing:border-box}
html,body{width:1200px;height:3056px;overflow:hidden}
body{position:relative;font-family:"Jost",sans-serif;color:var(--text);background:var(--light)}
.abs{position:absolute}
.photo{position:absolute}
.btn{position:absolute;display:flex;align-items:center;justify-content:center;border-radius:20px;font-size:16px;font-weight:500}
.btn-orange{background:var(--orange);color:var(--white)}
/* hero */
.hero{position:absolute;left:0;top:0;width:1200px;height:586px;background:var(--dark);overflow:hidden}
.hero-circle{position:absolute;left:124px;top:-167px;width:950px;height:950px;border-radius:50%;background:radial-gradient(circle at 40% 45%,#1a1e2a,#232836 70%)}
.logo{position:absolute;display:flex;align-items:center;gap:6px;color:var(--white)}
.logo-name{font-weight:600;letter-spacing:.5px}
.logo-mark{background:var(--white)}
.nav{position:absolute;top:22px;right:121px;display:flex;gap:27px;font-size:11px;font-weight:700;color:var(--white)}
.nav .active{color:var(--orange);border-bottom:1px solid var(--orange);padding-bottom:3px}
.hero h1{position:absolute;left:225px;top:178px;font-size:60px;line-height:57px;font-weight:700;color:var(--white)}
.hero h1 .dot{color:var(--orange)}
.hero .sub{position:absolute;left:225px;top:328px;font-size:19px;line-height:23px;color:var(--white)}
/* about */
.about{position:absolute;left:0;top:586px;width:1200px;height:434px;background:var(--white)}
.about .kicker{position:absolute;left:553px;top:72px;font-size:19px;font-weight:600;color:var(--ink)}
.about h2{position:absolute;left:553px;top:106px;font-size:37px;line-height:36px;font-weight:600;color:var(--ink)}
.about h2 span{color:var(--orange)}
.about p{position:absolute;left:553px;width:500px;font-size:13.5px;line-height:19.5px;color:#333}
/* services */
.services{position:absolute;left:0;top:1020px;width:1200px;height:458px;background:linear-gradient(160deg,#3d4350,#353a46)}
.services .intro{position:absolute;top:66px;width:1200px;text-align:center;font-size:17.5px;line-height:23px;font-weight:600;color:var(--white)}
.card{position:absolute;top:1175px;width:264px;height:380px;box-shadow:0 4px 10px rgba(0,0,0,.3);text-align:center;overflow:hidden}
.card h3{margin-top:24px;font-size:38px;line-height:34px;font-weight:700;color:#2d3442}
.card .tag{font-size:24px;line-height:24px;color:#2d3442}
.card .btn{left:53px;top:331px;width:156px;height:33px}
/* clients */
.clients-title{position:absolute;top:1628px;width:1200px;text-align:center;font-size:37px;font-weight:600;color:var(--ink)}
.client{position:absolute;top:1713px;display:flex;align-items:center;gap:6px;font-size:24px;font-weight:500;color:#2a2f3a}
.client i{display:block;width:14px;height:14px;background:#2a8fc6}
/* panel */
.panel{position:absolute;left:140px;top:1845px;width:924px;height:300px;border-radius:36px;background:var(--dark)}
.panel-divider{position:absolute;left:587px;top:1870px;width:2px;height:250px;background:rgba(255,255,255,.35)}
.panel h3{position:absolute;font-size:36px;line-height:39px;font-weight:700;color:var(--white)}
.panel-text{position:absolute;font-size:13.5px;line-height:19.6px;font-style:italic;color:var(--white)}
.panel-list{position:absolute;list-style:none;font-size:13.5px;line-height:19.6px;font-style:italic;color:var(--white);text-align:right}
.panel-list li::after{content:"";display:inline-block;width:7px;height:7px;border-radius:50%;background:var(--white);margin-left:10px;vertical-align:middle}
.more{position:absolute;font-size:13px;font-style:italic;color:var(--orange)}
/* testimonials */
.testi-title{position:absolute;left:124px;top:2250px;font-size:55px;font-weight:700;color:var(--ink)}
.thumb{position:absolute;top:2230px;width:47px;height:112px;background:linear-gradient(#cfcfcf,#9a9a9a)}
.thumb.active{width:83px;background:linear-gradient(#6f6a64,#3b3430);border-bottom:4px solid var(--orange)}
.quote-box{position:absolute;left:318px;top:2390px;width:566px;height:145px;background:#f4f4f5}
.quote-mark{position:absolute;left:350px;top:2398px;font-size:90px;line-height:90px;color:#d8d8d8;font-weight:700}
.quote-line{position:absolute;left:374px;width:476px;text-align:center;font-size:15px;color:#333;border-bottom:1px solid #ccc;padding-bottom:3px}
.author{position:absolute;top:2552px;width:1200px;text-align:center;font-size:16px;font-weight:600;color:var(--ink);line-height:18px}
.author small{display:block;font-size:12px;font-weight:400;color:#555;line-height:14px}
.dots{position:absolute;top:2603px;left:546px;display:flex;gap:17px}
.dots span{width:8px;height:8px;border-radius:50%;background:#a9a9a9}
.dots .on{background:var(--orange)}
/* footer */
.footer{position:absolute;left:0;top:2669px;width:1200px;height:387px;background:var(--dark);overflow:hidden}
.footer-circle{position:absolute;left:124px;top:-90px;width:950px;height:950px;border-radius:50%;background:#2b303c}
.footer .address{position:absolute;top:135px;width:1200px;text-align:center;font-size:17px;line-height:19px;font-weight:600;color:var(--white)}
.contact{position:absolute;top:196px;display:flex;align-items:center;gap:8px;font-size:16px;color:var(--white)}
.socials{position:absolute;top:254px;left:558px;display:flex;gap:6px}
.socials span{width:24px;height:24px;background:var(--orange)}
.footer-rule{position:absolute;left:124px;top:326px;width:952px;height:1px;background:rgba(255,255,255,.2)}
.copyright{position:absolute;top:349px;width:1200px;text-align:center;font-size:13px;color:#b9bcc4}
</style>
</head>
<body>

<header class="hero">
  <div class="hero-circle"></div>
  <div class="photo" role="img" aria-label="Portrait of Martin Olafsky in a light blue shirt" style="left:543px;top:47px;width:500px;height:539px;background:radial-gradient(ellipse at 50% 85%,#7da3d0,#4e6f99 55%,rgba(40,48,66,0) 80%)"></div>
  <div class="logo" style="left:119px;top:19px">
    <span class="logo-name" style="font-size:14px">Brivane</span>
    <span class="logo-mark" style="width:12px;height:12px"></span>
    <span style="font-size:8px">COMMUNICATIONS</span>
  </div>
  <nav class="nav">
    <span class="active">HOME</span><span>ABOUT</span><span>SERVICES</span><span>INDUSTRIES</span><span>PORTFOLIO</span><span>CLIENTS</span><span>CONTACT</span>
  </nav>
  <h1>Your voice,<br><span style="padding-left:87px">My words<span class="dot">.</span></span></h1>
  <p class="sub">Copywriting &amp; executive ghostwriting that<br>speaks for your vision &amp; your technology.</p>
  <div class="btn" style="left:301px;top:412px;width:156px;height:35px;background:var(--white);color:#222">Contact Now</div>
</header>

<section class="about">
  <div class="photo" role="img" aria-label="Portrait of Martin Olafsky in a brown jacket" style="left:133px;top:11px;width:371px;height:423px;background:linear-gradient(180deg,#c9b4a4 0%,#a4775a 55%,#7a5236 100%);border-radius:120px 120px 0 0"></div>
  <div class="kicker">About Me</div>
  <h2>Hi! I’m<br><span>Martin Olafsky</span></h2>
  <p style="top:198px;font-style:italic">In nearly two decades in the international marketing trenches, I've learned to rapidly define and internalize company messages - and to communicate them at eye-level.</p>
  <p style="top:255px">Born and raised in the US, I've lived and worked in Israel since 1990, and speak fluent Hebrew. I do all client writing myself, so my clients get one-on-one service and a personal guarantee of quality.</p>
  <div class="btn btn-orange" style="left:553px;top:343px;width:155px;height:34px">Read More</div>
</section>

<section class="services">
  <p class="intro">Based just north of Tel Aviv, Brivane Communications provides messaging,<br>collateral creation, creative, content marketing, and consulting to companies in Israel and abroad.</p>
</section>

<div class="card" style="left:159px;background:linear-gradient(180deg,#8fd4cc,#5fb2aa)">
  <div class="photo" role="img" aria-label="Child looking through binoculars" style="left:20px;top:130px;width:224px;height:250px;background:radial-gradient(ellipse at 50% 60%,#2c3d6a,#3f5482 60%,rgba(95,178,170,0) 75%)"></div>
  <h3 style="position:relative">Messaging</h3>
  <div class="tag" style="position:relative">The Value of a<br>Fresh Perspective</div>
  <div class="btn btn-orange">Read More</div>
</div>
<div class="card" style="left:470px;background:linear-gradient(180deg,#a7c9b9,#3e8a74)">
  <div class="photo" role="img" aria-label="Schoolgirl with backpack writing on a chalkboard" style="left:20px;top:140px;width:200px;height:240px;background:radial-gradient(ellipse at 45% 55%,#d7a56b,#7b5a40 55%,rgba(62,138,116,0) 78%)"></div>
  <h3 style="position:relative">Collateral</h3>
  <div class="tag" style="position:relative;color:#3c4d55">Concise,<br>Effective,<br>Creative</div>
  <div class="btn btn-orange">Read More</div>
</div>
<div class="card" style="left:779px;background:linear-gradient(180deg,#f7b90c,#f3a600)">
  <div class="photo" role="img" aria-label="Fisherman in a yellow raincoat giving a thumbs up" style="left:10px;top:130px;width:250px;height:250px;background:radial-gradient(ellipse at 50% 60%,#f3dc3a,#e8c000 55%,rgba(243,166,0,0) 78%)"></div>
  <h3 style="position:relative">Content<br>Marketing</h3>
  <div class="tag" style="position:relative;font-size:20px;margin-top:6px">Giving Voice to Your Vision</div>
  <div class="btn btn-orange">Read More</div>
</div>

<h2 class="clients-title">Meet Some Of Our Clients</h2>
<div class="client" style="left:119px">Ravelo<i style="border-radius:50%"></i></div>
<div class="client" style="left:293px"><i style="border-radius:50%"></i>Quillan</div>
<div class="client" style="left:463px;color:#e03a3e">Mertova</div>
<div class="client" style="left:637px;font-size:18px;color:#2a6fb0"><i></i>Shieldnest</div>
<div class="client" style="left:798px">Kindrift<i style="border-radius:50%"></i></div>
<div class="client" style="left:966px;font-size:19px;color:#2a6fb0">Halvora</div>

<section class="panel"></section>
<div class="panel-divider"></div>
<div class="photo" role="img" aria-label="Smiling man in shirt and tie with arms crossed" style="left:152px;top:1832px;width:184px;height:313px;background:linear-gradient(180deg,#c9a087 0%,#d3dcea 45%,#a9b9d2 100%);border-radius:40px 40px 0 36px"></div>
<div class="photo" role="img" aria-label="Businessman in a suit presenting with open hand" style="left:901px;top:1826px;width:163px;height:319px;background:linear-gradient(180deg,#d2b29a 0%,#2b3244 40%,#1b2030 100%);border-radius:40px 40px 36px 0"></div>
<h3 class="panel" style="all:unset;position:absolute;left:351px;top:1917px;font-size:36px;line-height:39px;font-weight:700;color:#fff">What I do</h3>
<p class="panel-text" style="left:356px;top:1964px;width:200px">In nearly two decades in the international marketing trenches, I've learned to rapidly define and internalize company messages - and to communicate them at eye-level.</p>
<span class="more" style="left:356px;top:2106px">Read More..</span>
<h3 style="position:absolute;left:610px;top:1910px;width:228px;text-align:right;font-size:36px;line-height:39px;font-weight:700;color:#fff">Why Choose<br>Me</h3>
<ul class="panel-list" style="left:600px;top:1999px;width:242px">
  <li>In nearly two decades in the</li>
  <li>international marketing trenches,</li>
  <li>I've learned to rapidly</li>
  <li>define and internalize company</li>
</ul>
<span class="more" style="left:811px;top:2106px">Read More..</span>

<h2 class="testi-title">Testimonials</h2>
<div class="thumb" role="img" aria-label="Client portrait" style="left:800px"></div>
<div class="thumb active" role="img" aria-label="Client portrait, selected" style="left:848px"></div>
<div class="thumb" role="img" aria-label="Client portrait" style="left:933px"></div>
<div class="thumb" role="img" aria-label="Client portrait" style="left:982px"></div>
<div class="thumb" role="img" aria-label="Client portrait" style="left:1030px"></div>
<div class="quote-box"></div>
<div class="quote-mark">”</div>
<p class="quote-line" style="top:2432px">Lorem ipsum dolor sit amet enim. Etiam ullamcorper. Suspendisse a</p>
<p class="quote-line" style="top:2460px">pellentesque dui, non felis. Maecenas malesuada elit lectus felis,</p>
<p class="quote-line" style="top:2488px">malesuada ultricies.</p>
<div class="author">Dorin Castell<small>VP Marketing, Velmont</small></div>
<div class="dots"><span></span><span class="on"></span><span></span><span></span><span></span></div>

<footer class="footer">
  <div class="footer-circle"></div>
  <div class="logo" style="left:0;top:70px;width:1200px;justify-content:center;flex-direction:column;gap:2px">
    <span style="display:flex;align-items:center;gap:8px"><span class="logo-name" style="font-size:30px">Brivane</span><span class="logo-mark" style="width:22px;height:22px"></span></span>
    <span style="font-size:13px;letter-spacing:1px">COMMUNICATIONS</span>
  </div>
  <p class="address">P.O. Box 5127<br>Harlen, Israel 40815</p>
  <div class="contact" style="left:431px">
    <svg width="18" height="18" viewBox="0 0 24 24" aria-hidden="true"><path d="M6.6 10.8a15 15 0 0 0 6.6 6.6l2.2-2.2a1 1 0 0 1 1-.25 11.4 11.4 0 0 0 3.6.57 1 1 0 0 1 1 1V20a1 1 0 0 1-1 1A17 17 0 0 1 3 4a1 1 0 0 1 1-1h3.5a1 1 0 0 1 1 1c0 1.25.2 2.45.57 3.57a1 1 0 0 1-.25 1z" fill="#ef6a0c"/></svg>
    +972-55-018-2290
  </div>
  <div class="contact" style="left:642px">
    <svg width="18" height="14" viewBox="0 0 24 18" aria-hidden="true"><rect x="1" y="1" width="22" height="16" fill="none" stroke="#ef6a0c" stroke-width="2"/><path d="M1 1l11 9 11-9" fill="none" stroke="#ef6a0c" stroke-width="2"/></svg>
    hello@brivane.example
  </div>
  <div class="socials">
    <span role="img" aria-label="Chirpline"></span><span role="img" aria-label="Facetree"></span><span role="img" aria-label="Linkwork"></span>
  </div>
  <div class="footer-rule"></div>
  <p class="copyright">© 2023 Brivane Communications | All Rights Reserved</p>
</footer>

</body>
</html>
```